Einzelne Suchwerk Landingpage
Suchwerk Landingpage für das Thema
„Vergleich von Private Rentenversicherungen“
Haupt Suchbegriffe für die die Landingpage verwendet werden soll:
-Private Rente
-Vergleich Private Rente
-Private Rentenversicherung
Mitbewerber:
Siehe Suchwerk Ergebnisse bei Eingabe obiger Suchbegriffe
Zielgruppe:
Alle Bundesbürger die sich mit privater Altersvorsorge beschäftigen.
Verstärkt Männer aber auch Frauen im Alter zwischen ca. 35-55 J.
Designanforderungen:
Spagat zwischen
Priorität I: ansprechenden des Besuchers auf emotionaler Ebene (Einbindung von Menschenbildern, etc.)
und
Priorität II: Ausdruck von Seriosität, Kompetenz und Unabhängigkeit
Als Beispiel-Designvorlagen von Mitbewerbern finde ich folgende Seite sehr ansprechend:
https://www1.ruhestand-kassenblick.de/ (hier ist mir nur das Formular zu groß, zu wenig Platz für Text)
Oder
http://www.geldlotse17.info/Sofortrente-Vergleich/index.html
(Design ist nicht so toll, aber klar strukturiert)
Vorlage für die Strukturierung der Seite:
Gute Erfahrungen was die Conversionsraten angeht habe ich mit der aktuell schon bestehenden Seite zum Thema „Rürup Rente“ gemacht.
www.kassenblick-basisplan-neu.de
Sicher ist diese was das Design angeht optimierungsfähig.
Was das Verhältnis Text/Formular angeht finde ich den Aufbau jedoch ganz gut bzw. hat sich die Seite bewährt. Die Unterseiten für Datenschutz und Impressum können ebenfalls übernommen werden.
Content
Der Text für die Seite ist hier hinterlegt:
www.wandoret.com/Inhalt_Text.docx
Formular:
Für das Formular könnten Sie ggf. auch den Quelltext der bestehenden Rürup Seite (s.o.) nutzen.
Das müsste dann nur minimal abgeändert werden.
www.wandoret.com/Formular.docx
Bei weiteren Rückfragen stehe ich gerne zur Verfügung.

```html
<!DOCTYPE html>
<html lang="de">
<head>
<meta charset="utf-8">
<title>Rentenblick-Vergleich.com</title>
<link rel="stylesheet" href="https://fonts.googleapis.com/css2?family=Arimo:wght@400;700&display=swap">
<style>
:root{
  --brand:#1a90c9;
  --brand-dark:#0b84bd;
  --panel:#f1f1ef;
  --text:#222;
  --field-border:#9a9a9a;
  --bg-blue:#5aaede;
  --bg-green:#6fa83a;
  --link:#0033cc;
}
*{box-sizing:border-box;margin:0;padding:0}
html,body{width:1200px;height:939px;overflow:hidden}
body{font-family:"Arimo",Arial,sans-serif;color:var(--text);position:relative}
.hero-photo{position:absolute;inset:0;background:linear-gradient(180deg,var(--bg-blue) 0%,var(--bg-green) 100%)}
.site-title{position:absolute;left:0;top:30px;width:494px;height:58px;background:var(--panel);
  padding:12px 0 0 36px;font-size:32px;line-height:34px;color:var(--brand);letter-spacing:-.2px;white-space:nowrap}
.site-tagline{position:absolute;left:0;top:88px;width:456px;height:27px;background:var(--panel);
  padding:5px 0 0 36px;font-size:15.5px;line-height:18px;color:var(--brand);white-space:nowrap}
.main-nav{position:absolute;left:0;top:133px;width:600px;height:26px;background:var(--panel);
  font-size:14px;color:var(--brand)}
.main-nav a{position:absolute;top:5px;color:inherit;text-decoration:none}
.content{position:absolute;left:34px;top:179px;width:566px;height:760px;background:var(--panel);
  padding:17px 52px 0 14px;font-size:13.6px;line-height:22.7px}
.content h2{font-size:14px;line-height:22.7px;color:var(--brand);font-weight:700}
.content p{margin-bottom:22.7px}
.configurator{position:absolute;left:654px;top:218px;width:357px;height:462px;background:#fff;
  box-shadow:0 2px 10px rgba(0,0,0,.35)}
.configurator .head{background:var(--panel);height:47px;padding:14px 0 0 17px;font-size:19.5px;line-height:22px;color:var(--brand)}
.form{position:absolute;left:0;top:48px;width:100%}
.row{display:flex;align-items:center;height:22.7px;font-size:10.5px;white-space:nowrap}
.row label{width:159px;text-align:right;padding-right:4px;flex:none}
.row .fields{display:flex;gap:4px;align-items:center}
.input{height:18px;border:1px solid var(--field-border);background:#fff}
.select{height:18px;border:1px solid #aaa;border-radius:3px;background:linear-gradient(#fff,#e6e6e6);
  position:relative;font-size:10px;padding:3px 0 0 6px;white-space:nowrap;overflow:hidden}
.select::before,.select::after{content:"";position:absolute;right:5px;border-left:3px solid transparent;border-right:3px solid transparent}
.select::before{top:4px;border-bottom:4px solid #333}
.select::after{top:10px;border-top:4px solid #333}
.privacy{position:absolute;left:7px;top:329px;font-size:9.5px;line-height:13px;width:220px}
.privacy .check{display:inline-block;width:12px;height:12px;border:1px solid #777;vertical-align:-2px;margin-right:8px}
.privacy a{color:var(--link);text-decoration:underline}
.cta{position:absolute;left:7px;top:398px;width:300px;height:43px;background:var(--brand-dark);
  color:#fff;font-size:20.5px;line-height:24px;font-weight:700;padding:10px 0 0 13px;letter-spacing:.2px}
.cta-arrow{position:absolute;left:294px;top:391px;width:58px;height:58px}
</style>
</head>
<body>
<div class="hero-photo" role="img" aria-label="Foto: blauer Sommerhimmel über einer grünen Wiese"></div>

<header>
  <div class="site-title">Rentenblick-Vergleich.com</div>
  <div class="site-tagline">kostenlos testen, welche pirivate Rente für Sie ideal ist</div>
</header>

<nav class="main-nav">
  <a style="left:34px">Start</a>
  <a style="left:124px">Links</a>
  <a style="left:217px">Kontakt</a>
  <a style="left:325px">Impressum</a>
  <a style="left:454px">Datenschutz</a>
</nav>

<main class="content">
  <h2>Lorem ipsum dolor sit amet</h2>
  <p>Onsectetuer adipiscing elit. Aenean commodo ligula eget dolor. Aenean massa. Cum sociis natoque penatibus et magnis dis parturient montes, nascetur ridiculus mus. Donec quam felis, ultricies nec, pellentesque eu, pretium quis, sem. Nulla consequat massa quis enim. Donec pede justo, fringilla vel, aliquet nec, vulputate eget, arcu. In enim justo, rhoncus ut, imperdiet a, venenatis vitae, justo. Nullam dictum felis eu pede mollis pretium. Integer tincidunt.</p>
  <h2>Cras dapibus</h2>
  <p>Vivamus elementum semper nisi. Aenean vulputate eleifend tellus. Aenean leo ligula, porttitor eu, consequat vitae, eleifend ac, enim. Aliquam lorem ante, dapibus in, viverra quis, feugiat a, tellus. Phasellus viverra nulla ut metus varius laoreet. Quisque rutrum. Aenean imperdiet. Etiam ultricies nisi vel augue. Curabitur ullamcorper ultricies nisi. Nam eget dui. Etiam rhoncus. Maecenas tempus, tellus eget condimentum rhoncus, sem quam semper libero, sit amet adipiscing sem neque sed ipsum. Nam quam nunc, blandit vel, luctus pulvinar, hendrerit id, lorem. Maecenas nec odio et ante tincidunt tempus. Donec vitae sapien ut libero venenatis faucibus. Nullam quis ante. Etiam sit amet orci eget eros faucibus tincidunt.</p>
  <h2>Aenean imperdiet</h2>
  <p>Etiam ultricies nisi vel augue. Curabitur ullamcorper ultricies nisi. Nam eget dui. Etiam rhoncus. Maecenas tempus, tellus eget condimentum rhoncus, sem quam semper libero, sit amet adipiscing sem neque sed ipsum. Nam quam nunc, blandit vel, luctus pulvinar, hendrerit id, lorem. Maecenas nec odio et ante tincidunt tempus.</p>
</main>

<aside class="configurator">
  <div class="head">Ihr Konfigurator</div>
  <div class="form">
    <div class="row"><label>Anlagebetrag (€/Zahlart):</label><div class="fields"><span class="input" style="width:79px"></span><span class="select" style="width:90px">monatlich</span></div></div>
    <div class="row"><label>Rentenauszahlung:</label><div class="fields">im Alter von <span class="input" style="width:59px"></span> Jahren</div></div>
    <div class="row"><label>Bruttoeinkommen (€/Jahr):</label><div class="fields"><span class="input" style="width:98px"></span></div></div>
    <div class="row"><label>Kinder:</label><div class="fields"><span class="select" style="width:172px">Bitte auswählen</span></div></div>
    <div class="row"><label>Familienstand:</label><div class="fields"><span class="select" style="width:172px">Bitte auswählen</span></div></div>
    <div class="row"><label>Beruf, Berufsstatus:</label><div class="fields"><span class="input" style="width:73px"></span><span class="select" style="width:95px">Angestellter</span></div></div>
    <div class="row"><label>Geburtsdatum:</label><div class="fields"><span class="select" style="width:39px">T</span><span class="select" style="width:73px">Monat</span><span class="select" style="width:51px">Jahr</span></div></div>
    <div class="row"><label>Anrede, Vorname, Name:</label><div class="fields"><span class="select" style="width:50px">Frau</span><span class="input" style="width:54px"></span><span class="input" style="width:58px"></span></div></div>
    <div class="row"><label>Straße, Hausnummer:</label><div class="fields"><span class="input" style="width:172px"></span></div></div>
    <div class="row"><label>PLZ, Wohnort:</label><div class="fields"><span class="input" style="width:39px"></span><span class="input" style="width:129px"></span></div></div>
    <div class="row"><label>Tel.-Nr. / Erreichbarkeit:</label><div class="fields"><span class="input" style="width:88px"></span><span class="select" style="width:80px">Ganztags</span></div></div>
    <div class="row"><label>eMail-Adresse:</label><div class="fields"><span class="input" style="width:172px"></span></div></div>
  </div>
  <div class="privacy">
    Sicherheit &amp; Datenschutz<br>
    Ihre Daten sind sicher und geschützt.<br>
    <span class="check"></span>Ich habe den <a>Datenschutz</a> gelesen und<br>akzeptiert.
  </div>
  <div class="cta">kostenlos testen</div>
  <svg class="cta-arrow" viewBox="0 0 58 58" aria-hidden="true">
    <circle cx="29" cy="29" r="28" fill="var(--brand-dark)" stroke="#fff" stroke-width="1.5"/>
    <path d="M23 16 L38 29 L23 42 Z" fill="#fff"/>
  </svg>
</aside>
</body>
</html>
```